Business card design needed for rebranded top-end landscaping business

We need a new business card design, incorporating our logo (colours Green #8dc63f and Grey #8a8c8e) and also some options that include the colour dark navy (eg #000040) as our uniforms are navy with white and grey trim.

We are an innovative landscaping company that maintains high-end gardens for meticulous clients. We pride ourselves on our customer service, our professionalism, and our workmanship.

Our business name needs to be easily read and our branding needs to be bold and memorable, without screaming "tradesman"! We prefer clean lines over lots of fine detail.

The design MUST include:
- Business name ("Brambleton Gardenworks")
- Logo (file uploaded)
- Employee name
- Phone number
- Email address
- www.brambletongardenworks.com.au
- Frondbook & Pictoleaf logos
- The Turfcraft Guild logo (file uploaded) along with the word "Member"
- Licence "Lic. 618392K"

OPTIONAL inclusions:
- "Creating outdoor spaces for our community to be inspired, refreshed and re-energised"
- "Landscape Maintenance - Irrigation - Arboriculture" (dashes can be replaced with dots or other)
- "Fully qualified, licensed & insured"
- "Residential - Strata - Commercial - Real Estate" (dashes can be replaced with dots or other)

High-end professionals and retirees, real estate agents

Landscaping

See Project description

Sans Serif

Designer to choose colors to be used in the design.

• Must incorporate our logo, and colours Green #8dc63f and Grey #8a8c8e) from the logo, and the colour DARK NAVY (eg #000040).
• The design MUST include:
• - Business name ("Brambleton Gardenworks")
• - Logo (file uploaded)
• - Employee name
• - Phone number
• - Email address
• - www.brambletongardenworks.com.au
• - Frondbook & Pictoleaf logos
• - The Turfcraft Guild logo (file uploaded) along with the word "Member"
• - Licence "Lic. 618392K"
• OPTIONAL inclusions:
• - "Creating outdoor spaces for our community to be inspired, refreshed and re-energised"
• - "Landscape Maintenance - Irrigation - Arboriculture" (dashes can be replaced with dots or other)
• - "Fully qualified, licensed & insured"
• - "Residential - Strata - Commercial - Real Estate" (dashes can be replaced with dots or other)

```html
<!DOCTYPE html>
<html lang="en">
<head>
<meta charset="utf-8">
<title>Brambleton Gardenworks – Business Card</title>
<link rel="stylesheet" href="https://fonts.googleapis.com/css2?family=Lato:wght@400;700;900&display=swap">
<style>
  :root {
    --green: #8dc63f;
    --green-deep: #6db33f;
    --grey: #8a8c8e;
    --grey-text: #6d6f71;
    --navy: #000040;
    --paper: #ffffff;
    --backdrop: #2b2f36;
  }
  * { margin: 0; padding: 0; box-sizing: border-box; }
  html, body {
    width: 1200px; height: 900px; overflow: hidden;
    background: var(--backdrop);
    font-family: "Lato", Arial, sans-serif;
  }
  .canvas { position: relative; width: 1200px; height: 900px; }

  .card {
    position: absolute; top: 285px;
    width: 540px; height: 330px;
    overflow: hidden;
    box-shadow: 0 10px 28px rgba(0,0,0,.45);
  }

  /* ---------- Front ---------- */
  .card-front { left: 40px; background: var(--paper); }

  .brand { position: absolute; left: 34px; top: 30px; display: flex; align-items: center; gap: 10px; }
  .brand-dot { width: 30px; height: 30px; border-radius: 50%; background: var(--green); }
  .brand-name { font-size: 21px; font-weight: 700; color: var(--grey); letter-spacing: .2px; }

  .contact { position: absolute; left: 34px; top: 84px; font-size: 11.5px; line-height: 1.5; color: var(--grey-text); font-style: normal; }
  .contact-company { color: var(--green-deep); }
  .contact-lines { margin-top: 8px; list-style: none; }
  .contact-lines li { display: flex; align-items: center; gap: 8px; }
  .contact-lines svg { width: 10px; height: 10px; flex: none; }

  .licence { position: absolute; left: 120px; top: 262px; font-size: 17px; color: var(--green-deep); }

  .person { position: absolute; left: 290px; top: 148px; }
  .person-name { font-size: 26px; font-weight: 900; color: var(--green-deep); letter-spacing: 1px; }
  .person-role { font-size: 13px; color: var(--navy); margin-top: 2px; letter-spacing: .3px; }

  .accent-bar { position: absolute; right: 0; top: 118px; width: 16px; height: 58px; background: var(--green-deep); }

  .social { position: absolute; left: 400px; top: 276px; display: flex; gap: 12px; font-size: 11px; color: var(--grey-text); }

  /* ---------- Back ---------- */
  .card-back { left: 620px; background: var(--grey); }
  .guild {
    position: absolute; left: 0; right: 0; top: 92px;
    display: flex; flex-direction: column; align-items: center;
  }
  .guild-square { width: 50px; height: 50px; background: var(--green); margin-bottom: 16px; }
  .guild-name { font-size: 28px; font-weight: 400; color: var(--navy); letter-spacing: 4px; }
  .guild-member {
    display: flex; align-items: center; gap: 10px; margin-top: 6px;
    font-size: 13px; color: var(--navy); letter-spacing: 2px;
  }
  .guild-member::before, .guild-member::after {
    content: ""; width: 70px; height: 1px; background: var(--navy);
  }
</style>
</head>
<body>
<main class="canvas">

  <section class="card card-front" aria-label="Business card front">
    <div class="brand">
      <span class="brand-dot"></span>
      <span class="brand-name">Brambleton Gardenworks</span>
    </div>

    <address class="contact">
      <div class="contact-company">Brambleton Gardenworks</div>
      <div>PO Box 1180 Linden Vale,</div>
      <div>NSW, 2590</div>
      <ul class="contact-lines">
        <li>
          <svg viewBox="0 0 10 10"><path d="M2 1 L4 1 L4.6 3.2 L3.4 4 Q4.4 6 6 6.6 L6.8 5.4 L9 6 L9 8 Q5 9.5 1 4 Z" fill="#8dc63f"/></svg>
          0412 555 301
        </li>
        <li>
          <svg viewBox="0 0 10 10"><rect x="0.5" y="2" width="9" height="6" fill="#8dc63f"/><path d="M0.5 2 L5 5.5 L9.5 2" fill="none" stroke="#fff" stroke-width="0.8"/></svg>
          info@brambletongardenworks.com.au
        </li>
        <li>
          <svg viewBox="0 0 10 10"><circle cx="5" cy="5" r="4.3" fill="none" stroke="#8dc63f" stroke-width="1"/><path d="M1 5 H9 M5 0.8 Q2.5 5 5 9.2 M5 0.8 Q7.5 5 5 9.2" fill="none" stroke="#8dc63f" stroke-width="0.8"/></svg>
          www.brambletongardenworks.com.au
        </li>
      </ul>
    </address>

    <div class="licence">Lic. 618392K</div>

    <div class="person">
      <div class="person-name">ELLIOT MARSH</div>
      <div class="person-role">Founder &amp; Director</div>
    </div>

    <div class="accent-bar"></div>

    <div class="social">
      <span>Frondbook</span>
      <span>Pictoleaf</span>
    </div>
  </section>

  <section class="card card-back" aria-label="Business card back">
    <div class="guild">
      <span class="guild-square"></span>
      <span class="guild-name">THE TURFCRAFT GUILD</span>
      <span class="guild-member">MEMBER</span>
    </div>
  </section>

</main>
</body>
</html>
```